FR banner

we need a banner design (36"x120" horizontal) that will be displayed on a local high school baseball field. My company ( Crestwell Prints Co) has been producing signage for the Fernmoor Ridge community since 2009. We would like to communicate that we do more than banners. The final design should include the slogan "Signs Shirts Swag" and our Logo.

Target Market(s)

companies, teams, events, shirt and other marketing items.

Industry/Entity Type

Sign, Print,

Font styles to use
Sans Serif

Requirements
Should not have
• no baseball content.

```html
<!DOCTYPE html>
<html lang="en">
<head>
<meta charset="utf-8">
<title>Crestwell Prints Co — Field Banner</title>
<link rel="stylesheet" href="https://fonts.googleapis.com/css2?family=Bebas+Neue&family=Krona+One&family=Oswald:wght@600&display=swap">
<style>
  :root {
    --page-bg: #3d3d3d;
    --panel-grey: #7b7b7b;
    --panel-sheen: #9a9a9a;
    --ink-black: #0c0c0c;
    --ink-white: #ffffff;
    --ink-light: #b3b3b3;
    --ink-mid: #777777;
  }
  * { margin: 0; padding: 0; box-sizing: border-box; }
  html, body {
    width: 1003px;
    height: 1200px;
    overflow: hidden;
    background: var(--page-bg);
  }
  .banner {
    position: absolute;
    left: 22px;
    top: 456px;
    width: 959px;
    height: 288px;
    background: linear-gradient(115deg, var(--panel-grey) 0%, var(--panel-grey) 60%, var(--panel-sheen) 72%, var(--panel-grey) 82%, #858585 100%);
    box-shadow: 0 6px 14px rgba(0,0,0,0.45);
    overflow: hidden;
  }
  .banner__field {
    position: absolute;
    left: 0;
    top: 0;
    width: 690px;
    height: 288px;
  }
  .brand {
    position: absolute;
    left: 46px;
    top: 104px;
    display: flex;
    align-items: center;
    gap: 12px;
  }
  .brand__dot {
    width: 22px;
    height: 22px;
    border-radius: 50%;
    background: var(--ink-white);
    flex: none;
  }
  .brand__name {
    font-family: "Krona One", sans-serif;
    font-size: 19px;
    line-height: 1.3;
    color: var(--ink-white);
    text-transform: uppercase;
  }
  .slogan {
    position: absolute;
    left: 282px;
    top: 36px;
    font-family: "Krona One", sans-serif;
    font-size: 55px;
    line-height: 70px;
    letter-spacing: -1px;
  }
  .slogan__line--signs { color: var(--ink-white); }
  .slogan__line--shirts { color: var(--ink-light); }
  .slogan__line--swag { color: var(--ink-mid); }
  .pitch {
    position: absolute;
    left: 702px;
    top: 36px;
    width: 240px;
  }
  .pitch__lead {
    font-family: "Bebas Neue", sans-serif;
    font-size: 52px;
    line-height: 44px;
    color: var(--ink-black);
  }
  .pitch__banners {
    font-family: "Oswald", sans-serif;
    font-weight: 600;
    font-size: 27px;
    line-height: 34px;
    color: var(--ink-white);
    letter-spacing: 0.5px;
  }
  .pitch__phone {
    display: flex;
    align-items: center;
    gap: 8px;
    margin-top: 6px;
    font-family: "Bebas Neue", sans-serif;
    font-size: 33px;
    line-height: 36px;
    color: var(--ink-white);
  }
  .pitch__phone svg { width: 24px; height: 24px; flex: none; }
  .pitch__web {
    margin-top: 8px;
    font-family: "Bebas Neue", sans-serif;
    font-size: 24px;
    line-height: 28px;
    color: var(--ink-black);
  }
</style>
</head>
<body>
  <div class="banner">
    <svg class="banner__field" viewBox="0 0 690 288" aria-hidden="true">
      <path fill="#0c0c0c" d="M6 10 L40 4 L120 8 L210 3 L330 7 L450 2 L560 6 L640 4 L662 10 L668 40 L662 70 L674 100 L666 140 L678 175 L668 210 L676 245 L664 272 L640 280 L540 284 L420 279 L300 285 L180 280 L80 284 L10 278 L4 240 L8 190 L2 140 L7 90 L3 45 Z"/>
    </svg>

    <div class="brand">
      <span class="brand__dot"></span>
      <div class="brand__name">Crestwell<br>Prints Co</div>
    </div>

    <div class="slogan">
      <div class="slogan__line--signs">SIGNS</div>
      <div class="slogan__line--shirts">SHIRTS</div>
      <div class="slogan__line--swag">SWAG</div>
    </div>

    <div class="pitch">
      <div class="pitch__lead">WE DO<br>MORE THAN</div>
      <div class="pitch__banners">BANNERS</div>
      <div class="pitch__phone">
        <svg viewBox="0 0 24 24" aria-hidden="true">
          <circle cx="12" cy="12" r="12" fill="#ffffff"/>
          <path fill="#0c0c0c" d="M8.2 5.5c.5-.3 1.1-.2 1.4.3l1.2 2.1c.3.5.2 1.1-.2 1.4l-.9.7c.6 1.5 1.8 2.8 3.3 3.4l.7-.9c.3-.4 1-.5 1.4-.2l2.1 1.2c.5.3.6.9.3 1.4l-.8 1.3c-.4.6-1.2.9-1.9.7-3.8-1.1-6.7-4-7.8-7.8-.2-.7.1-1.5.7-1.9z"/>
        </svg>
        <span>(555) 014-2290</span>
      </div>
      <div class="pitch__web">WWW.CRESTWELLPRINTS.COM</div>
    </div>
  </div>
</body>
</html>
```